Business Card Design needed for logo design project

Would like a professional business card for a company involved in financial and latest technologies including CAD design. We would like the card to convey professionalism and communicate that we are involved in up to date technology solutions.

Target Market(s)

Business 2 Business sales

Industry/Entity Type

Financial

Colors

Designer to choose colors to be used in the design.

Requirements
Must have
• Business Name
Logo
Name
Phone
Email
Nice to have
• Website

```html
<!DOCTYPE html>
<html lang="en">
<head>
<meta charset="utf-8">
<title>NOVARIQ Business Card</title>
<link href="https://fonts.googleapis.com/css2?family=Open+Sans:wght@400;600;700;800&display=swap" rel="stylesheet">
<style>
  :root {
    --brand-red: #d0141b;
    --brand-navy: #141a3c;
    --card-white: #ffffff;
    --page-bg: #e9e7e3;
    --ink: #1b1f3a;
  }
  * { margin: 0; padding: 0; box-sizing: border-box; }
  html, body {
    width: 1200px; height: 900px; overflow: hidden;
    background: var(--page-bg);
    font-family: "Open Sans", Arial, sans-serif;
  }
  .stage {
    width: 1200px; height: 900px;
    display: flex; flex-direction: column;
    align-items: center; justify-content: center; gap: 44px;
  }
  .card {
    position: relative;
    width: 620px; height: 354px;
    box-shadow: 0 6px 18px rgba(0,0,0,0.18);
    overflow: hidden;
  }
  .card-back { background: var(--brand-red); }
  .back-wordmark {
    position: absolute; left: 48px; bottom: 46px;
    display: flex; align-items: center; gap: 12px;
    color: var(--card-white);
    font-weight: 800; font-size: 58px; letter-spacing: 1px;
  }
  .wordmark-square {
    width: 20px; height: 20px; background: var(--card-white);
  }
  .card-front { background: var(--card-white); }
  .front-bands { position: absolute; inset: 0; }
  .front-wordmark {
    position: absolute; left: 66px; top: 168px;
    color: var(--brand-red);
    font-weight: 800; font-size: 44px; letter-spacing: 1px;
  }
  .divider {
    position: absolute; left: 276px; top: 88px;
    width: 3px; height: 112px;
    transform: rotate(-14deg);
    background: linear-gradient(to bottom, rgba(208,20,27,0), var(--brand-red) 45%, rgba(208,20,27,0));
  }
  .contact {
    position: absolute; left: 330px; top: 66px;
    color: var(--ink);
  }
  .contact-name {
    color: var(--brand-red); font-weight: 700; font-size: 15px;
    text-transform: uppercase; letter-spacing: 0.5px;
  }
  .contact-title { font-size: 13px; margin-bottom: 12px; margin-left: 10px; }
  .contact-list { list-style: none; margin-left: 26px; }
  .contact-list li {
    display: flex; align-items: center; gap: 8px;
    font-size: 14px; line-height: 20px;
  }
  .contact-list svg { width: 13px; height: 13px; flex: none; }
  .address {
    position: absolute; left: 188px; top: 272px;
    display: flex; align-items: center; gap: 8px;
    color: var(--brand-red); font-size: 14px; font-weight: 600;
  }
  .address svg { width: 16px; height: 16px; }
</style>
</head>
<body>
<main class="stage">
  <section class="card card-back" aria-label="Card back">
    <div class="back-wordmark"><span class="wordmark-square"></span>NOVARIQ</div>
  </section>

  <section class="card card-front" aria-label="Card front">
    <svg class="front-bands" viewBox="0 0 620 354" width="620" height="354" aria-hidden="true">
      <polygon points="0,0 290,0 302,36 0,36" fill="var(--brand-red)"/>
      <polygon points="300,0 620,0 620,36 312,36" fill="var(--brand-navy)"/>
      <polygon points="0,310 390,310 402,354 0,354" fill="var(--brand-red)"/>
      <polygon points="400,310 620,310 620,354 412,354" fill="var(--brand-navy)"/>
    </svg>

    <div class="front-wordmark">NOVARIQ</div>
    <div class="divider"></div>

    <div class="contact">
      <p class="contact-name">Daniel Reyes</p>
      <p class="contact-title">Manager</p>
      <ul class="contact-list">
        <li>
          <svg viewBox="0 0 16 16" aria-hidden="true"><path d="M3 1l3 3-2 2c1 2 3 4 5 5l2-2 3 3-2 3C6 15 1 10 1 3z" fill="var(--brand-red)"/></svg>
          +1 555 214 0387
        </li>
        <li>
          <svg viewBox="0 0 16 16" aria-hidden="true"><rect x="4" y="1" width="8" height="14" rx="1.5" fill="none" stroke="var(--brand-red)" stroke-width="1.6"/></svg>
          +1 555 630 9172
        </li>
        <li>
          <svg viewBox="0 0 16 16" aria-hidden="true"><rect x="1" y="3" width="14" height="10" fill="var(--brand-red)"/><path d="M1 3l7 6 7-6" fill="none" stroke="#fff" stroke-width="1.2"/></svg>
          daniel@novariq.com
        </li>
        <li>
          <svg viewBox="0 0 16 16" aria-hidden="true"><rect x="1" y="2" width="14" height="9" fill="none" stroke="var(--brand-red)" stroke-width="1.6"/><path d="M6 14h4M8 11v3" stroke="var(--brand-red)" stroke-width="1.6"/></svg>
          www.novariq.com
        </li>
      </ul>
    </div>

    <div class="address">
      <svg viewBox="0 0 16 16" aria-hidden="true"><path d="M8 1a4 4 0 0 1 4 4c0 3-4 7-4 7S4 8 4 5a4 4 0 0 1 4-4z" fill="var(--brand-navy)"/><circle cx="8" cy="5" r="1.4" fill="#fff"/><ellipse cx="8" cy="13.5" rx="6" ry="1.8" fill="none" stroke="var(--brand-navy)" stroke-width="1.2"/></svg>
      Unit 4, Harbor Lane, Easton, State, 40217
    </div>
  </section>
</main>
</body>
</html>
```